Business card design

I need my logo on this card, things I need the card to have on it
licensed and insured.
owner operators Derek & Milton Halvorsen
my phone number 5418237906
Disaster Recovery, Storm Damage Restoration, Proactive Disaster Plan Management, Roof Repair/Restoration Structural Repair and Reconstruction, Emergency Boarding and Tarping Service, Perimeter Fencing, Emergency Tree Removal,

```html
<!DOCTYPE html>
<html lang="en">
<head>
<meta charset="utf-8">
<title>Halvorsen's Construction L.L.C — Business Card</title>
<link rel="stylesheet" href="https://fonts.googleapis.com/css2?family=Montserrat:ital,wght@0,300;0,400;0,500;0,600;1,300;1,400;1,500;1,600&display=swap">
<style>
  :root {
    --brand-blue: #1396eb;
    --band-light: #1c97ea;
    --band-dark: #0b7cdc;
    --list-blue: #1a8fe3;
    --white: #ffffff;
    --page: #ffffff;
    --shadow: rgba(0, 0, 0, 0.28);
  }
  * { margin: 0; padding: 0; box-sizing: border-box; }
  html, body {
    width: 1200px;
    height: 2373px;
    overflow: hidden;
    background: var(--page);
    font-family: "Montserrat", sans-serif;
  }
  .canvas { position: relative; width: 1200px; height: 2373px; }

  .card {
    position: absolute;
    left: 164px;
    width: 874px;
    height: 500px;
    box-shadow: 0 4px 10px var(--shadow);
    overflow: hidden;
  }

  /* Front */
  .card-front { top: 984px; background: var(--brand-blue); color: var(--white); }
  .front-name {
    position: absolute;
    left: 0; right: 0; top: 268px;
    text-align: center;
    font-weight: 400;
    font-size: 74px;
    letter-spacing: 1px;
    line-height: 1;
  }
  .front-sub {
    position: absolute;
    left: 0; right: 0; top: 370px;
    text-align: center;
    font-weight: 400;
    font-size: 24px;
    letter-spacing: 17px;
    padding-left: 17px;
  }
  .front-tagline {
    position: absolute;
    left: 0; right: 0; top: 430px;
    text-align: center;
    font-style: italic;
    font-weight: 500;
    font-size: 29px;
  }
  .edge-tick {
    position: absolute;
    top: 441px;
    height: 10px;
    background: var(--white);
  }
  .edge-tick.left { left: 0; width: 60px; }
  .edge-tick.right { right: 0; width: 67px; }

  /* Back */
  .card-back { top: 1648px; background: var(--white); }
  .back-band {
    position: absolute;
    left: 0; top: 0;
    width: 874px; height: 252px;
    background:
      linear-gradient(160deg, rgba(255,255,255,0.06) 0 40%, rgba(0,0,0,0) 40% 100%),
      linear-gradient(200deg, rgba(0,0,0,0) 0 55%, rgba(0,0,0,0.05) 55% 100%),
      linear-gradient(100deg, var(--band-light), var(--band-dark) 70%, var(--band-light));
    color: var(--white);
  }
  .band-tab {
    position: absolute;
    left: 0; top: 33px;
    width: 20px; height: 69px;
    background: var(--white);
  }
  .owner-names {
    position: absolute;
    left: 46px; top: 46px;
    font-weight: 500;
    font-size: 34px;
    letter-spacing: 0.3px;
    white-space: nowrap;
  }
  .owner-role {
    position: absolute;
    left: 198px; top: 88px;
    font-style: italic;
    font-weight: 300;
    font-size: 21px;
  }
  .phone-row {
    position: absolute;
    left: 53px; top: 153px;
    display: flex;
    align-items: center;
    gap: 14px;
  }
  .phone-icon { width: 60px; height: 60px; }
  .phone-number {
    font-weight: 600;
    font-size: 34px;
    letter-spacing: 0.5px;
  }
  .band-company {
    position: absolute;
    right: 28px; top: 84px;
    width: 250px;
    text-align: center;
    font-weight: 500;
    font-size: 30px;
    line-height: 1.25;
  }

  .service-list {
    position: absolute;
    list-style: none;
    color: var(--list-blue);
    font-style: italic;
    font-weight: 600;
    font-size: 17.5px;
    line-height: 1.25;
  }
  .service-list li { position: relative; padding-left: 20px; margin-bottom: 18px; }
  .service-list li::before {
    content: "";
    position: absolute;
    left: 0; top: 6px;
    width: 9px; height: 9px;
    border-radius: 50%;
    background: var(--list-blue);
  }
  .services-left { left: 42px; top: 286px; }
  .services-right { left: 526px; top: 284px; }
</style>
</head>
<body>
<main class="canvas">

  <section class="card card-front" aria-label="Card front">
    <h1 class="front-name">HALVORSEN'S</h1>
    <p class="front-sub">CONSTRUCTION L.L.C</p>
    <p class="front-tagline">licensed and insured</p>
    <span class="edge-tick left"></span>
    <span class="edge-tick right"></span>
  </section>

  <section class="card card-back" aria-label="Card back">
    <header class="back-band">
      <span class="band-tab"></span>
      <h2 class="owner-names">DEREK &amp; MILTON HALVORSEN</h2>
      <p class="owner-role">OWNER OPERATORS</p>
      <div class="phone-row">
        <svg class="phone-icon" viewBox="0 0 60 60" aria-hidden="true">
          <circle cx="30" cy="30" r="30" fill="#ffffff"/>
          <path d="M22 16c1.5-1 3-.6 3.8.8l2.6 4.6c.7 1.3.4 2.7-.8 3.6l-2 1.5c1.3 3.3 4 6.2 7.3 7.7l1.6-1.9c.9-1.1 2.4-1.4 3.6-.7l4.6 2.5c1.4.8 1.8 2.4.9 3.8l-1.6 2.5c-1.3 2-3.7 2.9-6 2.2C27 40 20 33 17.2 24.6c-.7-2.3.2-4.8 2.2-6.1z" fill="#1a8fe3"/>
        </svg>
        <span class="phone-number">5418237906</span>
      </div>
      <p class="band-company">HALVORSEN'S<br>CONSTRUCTION</p>
    </header>

    <ul class="service-list services-left">
      <li>DISASTER RECOVERY,</li>
      <li>STORM DAMAGE RESTORATION,</li>
      <li>PROACTIVE DISASTER PLAN MANAGEMENT</li>
      <li>ROOF REPAIR/RESTORATION<br>STRUCTURAL REPAIR AND RECONSTRUCTION</li>
    </ul>
    <ul class="service-list services-right">
      <li>PERIMETER FENCING</li>
      <li>EMERGENCY TREE REMOVAL</li>
      <li>EMERGENCY BOARDING<br>AND TARPING SERVICE,</li>
    </ul>
  </section>

</main>
</body>
</html>
```